Design a Flyer and Business Card for an Entertainment Company to use at a Wedding Expo

RK Entertainment is an entertainment company specialising in bands and other forms of public entertainment for functions and events (see rkentertainment.com.au).

Velvet Tide is one of their leading bands (see velvettide.com.au).

I need 2 flyers (one for each company) and a business card for RK Entertainment ready to print by this Thursday, 18th of June.

* The flyers must be targeted at the wedding market (any couples looking for entertainment for their wedding).
* The content on the existing flyers needs to be improved. Copywriting skills are essential.
* The Marrowby Hall (marrowbyhall.com) is a primary sponsor and their logo needs to be prominent on the flyer.
* The flyers and the business card need the phone numbers updated: office 02 9463 2758, mobile 0427 836 415
* Overall, the design should be consistent with the existing websites

```html
<!DOCTYPE html>
<html lang="en">
<head>
<meta charset="utf-8">
<title>RK Entertainment – Business Card</title>
<link rel="stylesheet" href="https://fonts.googleapis.com/css2?family=Oswald:wght@300;400;500&display=swap">
<style>
  :root {
    --page: #ffffff;
    --card-dark: #000000;
    --card-light: #ffffff;
    --gold: #c08a45;
    --ink: #111111;
    --white: #ffffff;
    --edge-dark: #8a2a3a;
    --edge-light: #bdbdbd;
  }
  * { margin: 0; padding: 0; box-sizing: border-box; }
  html, body {
    width: 981px;
    height: 1200px;
    overflow: hidden;
    background: var(--page);
    font-family: "Oswald", "Arial Narrow", sans-serif;
  }
  .canvas { position: relative; width: 981px; height: 1200px; }

  .card {
    position: absolute;
    left: 149px;
    width: 683px;
    height: 391px;
  }
  .card--front {
    top: 113px;
    background: var(--card-dark);
    border: 2px solid var(--edge-dark);
  }
  .card--back {
    top: 680px;
    background: var(--card-light);
    border: 1.5px solid var(--edge-light);
  }

  .tagline {
    position: absolute;
    left: 24px;
    top: 42px;
    font-weight: 400;
    font-size: 20px;
    letter-spacing: 7.6px;
    color: var(--gold);
    white-space: nowrap;
  }

  .brand {
    position: absolute;
    display: flex;
    align-items: center;
    gap: 12px;
    white-space: nowrap;
    font-weight: 400;
    text-transform: uppercase;
  }
  .brand__square { width: 34px; height: 34px; flex: none; }
  .brand__name { letter-spacing: 1px; }

  .card--front .brand { right: 34px; top: 262px; }
  .card--front .brand__square { background: var(--white); }
  .card--front .brand__name { color: var(--white); font-size: 40px; }

  .card--back .brand { left: 24px; top: 244px; }
  .card--back .brand__square { background: var(--ink); }
  .card--back .brand__name { color: var(--ink); font-size: 36px; }

  .rule {
    position: absolute;
    left: 24px;
    right: 34px;
    height: 2px;
    background: var(--gold);
  }
  .card--front .rule { top: 360px; }
  .card--back .rule { top: 316px; }

  .contact {
    position: absolute;
    left: 376px;
    top: 70px;
    color: var(--ink);
  }
  .contact__name {
    font-size: 22px;
    font-weight: 400;
    letter-spacing: 2.5px;
    color: var(--gold);
    line-height: 1.2;
  }
  .contact__role {
    font-size: 19px;
    font-weight: 400;
    letter-spacing: 2px;
    line-height: 1.3;
    margin-bottom: 10px;
  }
  .contact__line {
    font-size: 16px;
    font-weight: 300;
    line-height: 36px;
    letter-spacing: 0.5px;
  }
  .contact__label { color: var(--gold); }
  .contact__email { font-size: 15px; font-weight: 300; line-height: 36px; }

  .address {
    position: absolute;
    left: 24px;
    top: 338px;
    font-size: 18px;
    font-weight: 400;
    letter-spacing: 5.6px;
    color: var(--ink);
    white-space: nowrap;
  }
</style>
</head>
<body>
<main class="canvas">

  <section class="card card--front" aria-label="Business card front">
    <p class="tagline">THE WEDDING ENTERTAINMENT SPECIALISTS</p>
    <div class="brand">
      <span class="brand__square" aria-hidden="true"></span>
      <span class="brand__name">RK Entertainment</span>
    </div>
    <div class="rule" aria-hidden="true"></div>
  </section>

  <section class="card card--back" aria-label="Business card back">
    <div class="contact">
      <p class="contact__name">LIAM CARTER</p>
      <p class="contact__role">SALES REPRESENTATIVE</p>
      <p class="contact__line"><span class="contact__label">(O)</span> 02 9463 2758</p>
      <p class="contact__line"><span class="contact__label">(M)</span> 0427 836 415</p>
      <p class="contact__email">www.info@rkentertainment.com.au</p>
    </div>
    <div class="brand">
      <span class="brand__square" aria-hidden="true"></span>
      <span class="brand__name">RK Entertainment</span>
    </div>
    <div class="rule" aria-hidden="true"></div>
    <p class="address">000 ADDRESS STREET&nbsp;&nbsp;&nbsp;ANY CITY, STATE&nbsp;&nbsp;0000</p>
  </section>

</main>
</body>
</html>
```